Business Stationery for Bramwell Oakes Recruitment Ltd
Marnie Thwaite
Cutting-Edge
Director
42 Quillmere Road
Teddington
Middlesex
KT4 9RW
marnie@bramwelloakes.co.uk
www.bramwelloakes.co.uk
Please use attached logo - I require the business card and company stationery - cutting edge design please

```html
<!DOCTYPE html>
<html lang="en">
<head>
<meta charset="utf-8">
<title>Bramwell Oakes Recruitment – Business Card</title>
<link rel="stylesheet" href="https://fonts.googleapis.com/css2?family=Cinzel:wght@400;600&family=Lato:wght@400;700&display=swap">
<style>
  :root {
    --navy: #2b2c7e;
    --navy-deep: #1c1d5c;
    --navy-light: #3d3f9c;
    --paper: #ffffff;
    --ink: #2a2b6e;
    --grey: #6d6f80;
    --backdrop: #ecebe8;
  }
  * { box-sizing: border-box; margin: 0; padding: 0; }
  html, body { width: 1200px; height: 629px; overflow: hidden; }
  body {
    background: var(--backdrop);
    font-family: "Lato", sans-serif;
    display: flex;
    align-items: center;
    justify-content: center;
    gap: 60px;
  }
  .card {
    width: 500px;
    height: 323px;
    position: relative;
    overflow: hidden;
    box-shadow: 0 6px 20px rgba(0,0,0,0.15);
  }
  /* Front */
  .card-front {
    background: radial-gradient(ellipse at 50% 40%, var(--navy-light) 0%, var(--navy) 55%, var(--navy-deep) 100%);
    color: var(--paper);
    display: flex;
    align-items: center;
    justify-content: center;
  }
  .front-brand {
    font-family: "Cinzel", serif;
    font-weight: 400;
    font-size: 34px;
    letter-spacing: 4px;
    color: var(--paper);
  }
  .front-web {
    position: absolute;
    left: 30px;
    bottom: 24px;
    font-size: 10px;
    letter-spacing: 3px;
    text-transform: uppercase;
    color: rgba(255,255,255,0.85);
  }
  /* Back */
  .card-back { background: var(--paper); color: var(--ink); }
  .back-wave { position: absolute; left: 0; bottom: 0; width: 500px; height: 110px; }
  .brand {
    position: absolute;
    left: 34px;
    top: 56px;
    display: flex;
    align-items: center;
    gap: 12px;
  }
  .brand-square { width: 14px; height: 14px; background: var(--navy); flex: none; }
  .brand-name {
    font-family: "Cinzel", serif;
    font-weight: 600;
    font-size: 18px;
    letter-spacing: 1.5px;
    color: var(--navy);
    white-space: nowrap;
  }
  .person {
    position: absolute;
    left: 34px;
    top: 140px;
  }
  .person-name {
    font-family: "Cinzel", serif;
    font-weight: 600;
    font-size: 13px;
    letter-spacing: 2px;
    color: var(--navy);
  }
  .person-role { font-size: 10px; color: var(--grey); margin-top: 3px; letter-spacing: 1px; }
  .contacts {
    position: absolute;
    left: 268px;
    top: 120px;
    list-style: none;
    font-size: 10.5px;
    color: var(--ink);
  }
  .contacts li { display: flex; align-items: center; gap: 8px; margin-bottom: 7px; }
  .contacts svg { width: 11px; height: 11px; flex: none; }
  .address {
    position: absolute;
    left: 34px;
    top: 200px;
    font-size: 9.5px;
    color: var(--grey);
    letter-spacing: 0.5px;
  }
  .back-web {
    position: absolute;
    right: 30px;
    bottom: 18px;
    font-size: 10px;
    letter-spacing: 3px;
    text-transform: uppercase;
    color: var(--paper);
  }
</style>
</head>
<body>
  <section class="card card-front" aria-label="Card front">
    <div class="front-brand">Bramwell Oakes</div>
    <div class="front-web">www.bramwelloakes.co.uk</div>
  </section>

  <section class="card card-back" aria-label="Card back">
    <svg class="back-wave" viewBox="0 0 500 110" preserveAspectRatio="none" aria-hidden="true">
      <path d="M0 110 L0 96 C150 92 330 70 500 20 L500 110 Z" fill="var(--navy)"/>
      <path d="M0 92 C150 88 330 64 500 12" fill="none" stroke="var(--navy-light)" stroke-width="1.5"/>
    </svg>

    <div class="brand">
      <span class="brand-square"></span>
      <div class="brand-name">Bramwell Oakes Recruitment</div>
    </div>

    <div class="person">
      <div class="person-name">MARNIE THWAITE</div>
      <div class="person-role">Director</div>
    </div>

    <ul class="contacts">
      <li>
        <svg viewBox="0 0 12 12"><rect width="12" height="12" fill="var(--navy)"/><path d="M3.5 2.5h1.5l.7 2-1 .7a5 5 0 0 0 2.1 2.1l.7-1 2 .7v1.5a1 1 0 0 1-1 1A6.5 6.5 0 0 1 2.5 3.5a1 1 0 0 1 1-1z" fill="#fff"/></svg>
        T 020 7946 0321
      </li>
      <li>
        <svg viewBox="0 0 12 12"><rect width="12" height="12" fill="var(--navy)"/><rect x="4" y="2" width="4" height="8" rx="0.8" fill="#fff"/></svg>
        M 07700 900482
      </li>
      <li>
        <svg viewBox="0 0 12 12"><rect width="12" height="12" fill="var(--navy)"/><path d="M2.5 3.5h7v5h-7z M2.5 3.5l3.5 3 3.5-3" fill="none" stroke="#fff" stroke-width="0.9"/></svg>
        marnie@bramwelloakes.co.uk
      </li>
      <li>
        <svg viewBox="0 0 12 12"><rect width="12" height="12" fill="var(--navy)"/><path d="M6 2a2.5 2.5 0 0 1 2.5 2.5C8.5 7 6 10 6 10S3.5 7 3.5 4.5A2.5 2.5 0 0 1 6 2z" fill="#fff"/></svg>
        Teddington, Middlesex
      </li>
    </ul>

    <div class="address">42 Quillmere Road, Teddington, Middlesex KT4 9RW</div>
    <div class="back-web">www.bramwelloakes.co.uk</div>
  </section>
</body>
</html>
```